Website Design - for Energy Efficiency company - large corporate feel

Hi there,
Thanks for checking out this project!
We're a UK based energy efficiency business. We arrange for energy efficient systems to be fitted in people's houses (i.e. efficient boilers, solar panels etc.) However, we do not install them ourselves as we have accredited installers who install on our behalf. Therefore the website should appeal to these businesses and have a very professional corporate feel. The final design should communicate that we are a financially safe large corporation.
Our existing website should not be used for inspiration as the style and content are very outdated (it was from a time when were installers - which we no longer are).
The new website design should use the greens from our logo, however I don't want the site saturated in this colour.
I'm really open to your chosen layout and therefore I'm not a huge fan of including links to websites I like - as I don't want to limit your own creativity. However, I would like it to look corporate (but not too boring and unimaginative).
So here's a few links to websites that I feel give a feel of financially safe / large corporate etc. Although you certainly don't have to design with this style / layout in mind:
http://www.brelvanhub.org.uk/advice
http://www.tolvenrise.co.uk/
http://www.qpwd.org.uk/
http://www.wendrowkeyplot.co.uk/
http://www.ruvasto.co.uk/ (very bad design but looks corporate)
http://www.pellarwatt.org.uk/
http://www.vq.co.uk/ (looks corporate but too busy and boring)
http://www.quellisto.co.uk/business/index.htm
http://www.dormavel.com/
https://www.ostrevan.com/en/index.html
The site is for 4 different audiences:
Consumers | Businesses | Public Sector | Installers
Therefore, it's important that there is some form of way of splitting the site up into these sections (almost like 4 websites in 1). Each section will then have the navigation menu with 7 links.
I've attached our logo (company-logo.jpg) and another logo design we have to display inline with regulations (blue-pact-logo.jpg).
Happy designing, and thank you!

```html
<!DOCTYPE html>
<html lang="en">
<head>
<meta charset="utf-8">
<title>Leafridge Energy</title>
<link rel="stylesheet" href="https://fonts.googleapis.com/css2?family=Open+Sans:ital,wght@0,300;0,400;0,600;0,700;0,800;1,400&display=swap">
<style>
:root{
  --green:#4f7f1f;
  --green-band:#5a8a25;
  --green-bright:#6fb52c;
  --ink:#222;
  --text:#444;
  --muted:#666;
  --header:#262626;
  --header-active:#141414;
  --panel-grey:#ececec;
  --rule:#dcdcdc;
  --soft:#f2f2f2;
}
*{box-sizing:border-box;margin:0;padding:0}
html,body{width:946px;height:1200px;overflow:hidden;background:#fff}
body{font-family:"Open Sans",Arial,sans-serif;color:var(--text);position:relative}
a{color:inherit;text-decoration:none}

.site-header{position:absolute;top:0;left:0;width:946px;height:72px;background:var(--header)}
.brand{position:absolute;left:78px;top:18px;display:flex;align-items:center;gap:8px}
.brand-mark{width:34px;height:34px;border-radius:50%;background:var(--green-bright)}
.brand-name{font-size:21px;font-weight:700;color:var(--green-bright);letter-spacing:.5px;line-height:1}
.main-nav{position:absolute;left:338px;top:0;height:72px;display:flex}
.main-nav a{display:flex;align-items:center;height:72px;padding:0 10.5px;color:#fff;font-size:10.4px}
.main-nav a.is-active{background:var(--header-active);padding:0 11px}

.hero{position:absolute;top:72px;left:0;width:946px;height:369px;
  background:linear-gradient(180deg,#c9d8e8 0%,#a7bccf 22%,#5f7895 40%,#2c3d63 62%,#1c2748 85%,#2a3550 100%)}
.hero-title{position:absolute;left:78px;top:208px;font-size:33px;font-weight:800;letter-spacing:-1.6px;line-height:35px;color:#111}
.hero-cta{position:absolute;left:78px;top:290px;width:75px;height:29px;background:var(--green-bright);border:1px solid #4a8a1c;border-radius:2px;color:#123;font-size:12px;display:flex;align-items:center;justify-content:center;letter-spacing:-.3px}
.hero-dots{position:absolute;left:813px;top:345px;display:flex;gap:3px}
.hero-dots span{width:11px;height:11px;border-radius:50%;background:rgba(255,255,255,.45)}
.hero-dots span:first-child{background:#fff}
.hero-rule{position:absolute;top:441px;left:0;width:946px;height:5px;background:var(--green-band)}

.section-band{position:absolute;left:0;width:946px}
.band-soft{top:446px;height:30px;background:var(--soft)}
.band-green{top:770px;height:26px;background:var(--green-band)}
.section-title{position:absolute;background:#fff;box-shadow:0 2px 3px rgba(0,0,0,.18);color:var(--green);font-weight:600;letter-spacing:-.6px;display:flex;align-items:center;justify-content:center}
.title-services{left:399px;top:459px;width:149px;height:35px;font-size:19px}
.title-welcome{left:324px;top:779px;width:298px;height:34px;font-size:19px}

.services-intro{position:absolute;left:80px;top:504px;width:786px;text-align:center;font-size:14.3px;font-weight:300;line-height:19px;color:#444}
.audiences{position:absolute;top:566px;left:0;width:946px}
.audience{position:absolute;width:160px;text-align:center}
.audience-photo{width:110px;height:110px;margin:0 auto;border-radius:50%;border:6px solid var(--green-band);box-shadow:inset 0 0 0 3px #fff}
.audience-name{margin-top:7px;font-size:17.5px;font-weight:300;color:#222;letter-spacing:-.3px}
.small-btn{display:inline-block;margin-top:8px;padding:3px 5px;border:1px solid #cfcfcf;font-size:9.2px;color:var(--green);letter-spacing:-.2px}

.welcome-copy{position:absolute;left:78px;top:824px;width:790px;text-align:center;font-size:9.8px;line-height:16.3px;color:#555;letter-spacing:-.15px}
.welcome-rule{position:absolute;left:79px;top:916px;width:788px;height:1px;background:var(--rule)}
.welcome-btn{position:absolute;left:437px;top:903px;width:71px;height:25px;border:1px solid #cfcfcf;background:#fff;color:var(--green);font-size:11px;display:flex;align-items:center;justify-content:center}

.info-panel{position:absolute;left:79px;top:943px;width:788px;height:194px;border:1px solid var(--rule);border-radius:14px;overflow:hidden}
.panel-head{position:absolute;top:0;left:0;width:100%;height:38px;background:var(--panel-grey)}
.panel-divider{position:absolute;left:463px;top:38px;width:1px;height:156px;background:var(--rule)}
.panel-heading{position:absolute;top:9px;font-size:17.5px;font-weight:700;color:#111;letter-spacing:-.5px}
.products{position:absolute;left:0;top:0}
.product{position:absolute;width:210px}
.product-thumb{position:absolute;left:0;top:0;width:51px;height:51px}
.product-name{position:absolute;left:61px;top:-3px;font-size:14.5px;color:var(--green);white-space:nowrap;letter-spacing:-.2px}
.product-text{position:absolute;left:63px;top:18px;width:150px;font-size:9.2px;line-height:11.2px;color:#444}
.testimonial{position:absolute;left:500px;width:270px}
.quote-open,.quote-close{position:absolute;color:var(--green);font-size:20px;font-weight:700;font-family:Georgia,serif;line-height:1}
.quote-open{left:0;top:-3px}
.quote-close{left:260px;top:40px}
.testimonial p{margin-left:16px;font-size:10.6px;font-style:italic;line-height:15px;color:#555;width:250px}
.testimonial b{font-style:normal;font-weight:700;color:#222}

.site-footer{position:absolute;top:1153px;left:0;width:946px;text-align:center;font-size:8.6px;color:#666}
.footer-nav a{padding:0 4px}
.footer-nav span{color:#999}
.copyright{margin-top:5px}
</style>
</head>
<body>
<header class="site-header">
  <a class="brand" href="#"><span class="brand-mark"></span><span class="brand-name">LEAFRIDGE ENERGY</span></a>
  <nav class="main-nav">
    <a class="is-active" href="#">Home</a>
    <a href="#">What’s Blue Pact</a>
    <a href="#">Homeowners</a>
    <a href="#">Tenanats</a>
    <a href="#">Landlords</a>
    <a href="#">Book Assessment</a>
    <a href="#">Contact Us</a>
  </nav>
</header>

<section class="hero" role="img" aria-label="Worker fitting solar panels on a rooftop beside the sea">
  <h1 class="hero-title">THE BLUE PACT -<br>IT'S HERE, IT'S HAPPENING</h1>
  <a class="hero-cta" href="#">Know more</a>
  <div class="hero-dots"><span></span><span></span><span></span><span></span></div>
</section>
<div class="hero-rule"></div>

<div class="section-band band-soft"></div>
<h2 class="section-title title-services">Our Services</h2>
<p class="services-intro">Contrairement à une opinion répandue, le Lorem Ipsum n'est pas simplement du texte aléatoire. Il trouve ses racines dans une oeuvre de la littérature</p>

<div class="audiences">
  <div class="audience" style="left:76px">
    <div class="audience-photo" role="img" aria-label="Smiling consumer in front of solar panels" style="background:radial-gradient(circle at 40% 40%,#7fb0e0,#2f6fb5 70%)"></div>
    <div class="audience-name">Consumers</div>
    <a class="small-btn" href="#">Know more</a>
  </div>
  <div class="audience" style="left:287px">
    <div class="audience-photo" role="img" aria-label="Wall-mounted boiler" style="background:radial-gradient(circle at 50% 45%,#f4f4f2,#c9c8c2 75%)"></div>
    <div class="audience-name">Businesses</div>
    <a class="small-btn" href="#">Know more</a>
  </div>
  <div class="audience" style="left:499px">
    <div class="audience-photo" role="img" aria-label="Insulation board being fitted to a wall" style="background:radial-gradient(circle at 45% 45%,#e8d9c0,#a88a66 75%)"></div>
    <div class="audience-name">Public Sector</div>
    <a class="small-btn" href="#">Know more</a>
  </div>
  <div class="audience" style="left:710px">
    <div class="audience-photo" role="img" aria-label="Installer working on heating pipework" style="background:radial-gradient(circle at 55% 45%,#6d8fc4,#6b4a3a 75%)"></div>
    <div class="audience-name">Installers</div>
    <a class="small-btn" href="#">Know more</a>
  </div>
</div>

<div class="section-band band-green"></div>
<h2 class="section-title title-welcome">Welcome to Leafridge Energy</h2>
<p class="welcome-copy">On sait depuis longtemps que travailler avec du texte lisible et contenant du sens est source de distractions, et empêche de se concentrer sur la mise en page elle-même. L'avantage du Lorem Ipsum sur un texte générique comme 'Du texte. Du texte. Du texte.' est qu'il possède une distribution de lettres plus ou moins normale, et en tout cas comparable avec celle du français standard. De nombreuses suites logicielles de mise en page ou éditeurs de sites Web ont fait du Lorem Ipsum leur faux texte par défaut, et une recherche pour 'Lorem Ipsum' vous conduira vers de nombreux sites qui n'en sont encore qu'à leur phase de construction. Plusieurs versions</p>
<div class="welcome-rule"></div>
<a class="welcome-btn" href="#">Know more</a>

<section class="info-panel">
  <div class="panel-head"></div>
  <div class="panel-divider"></div>
  <h3 class="panel-heading" style="left:15px">Our Products</h3>
  <h3 class="panel-heading" style="left:498px">Testimonials</h3>

  <div class="product" style="left:15px;top:58px">
    <div class="product-thumb" role="img" aria-label="Boiler units" style="background:linear-gradient(135deg,#8a7a6a,#3e3a36)"></div>
    <div class="product-name">Boilers</div>
    <p class="product-text">Lorem ipsum dolor sit amet, consectetur adipisicing elit, sed do eiusmod tempor.</p>
  </div>
  <div class="product" style="left:237px;top:58px">
    <div class="product-thumb" role="img" aria-label="Solid wall insulation layers" style="background:linear-gradient(135deg,#b9a99a,#6e5f55)"></div>
    <div class="product-name">Solid Wall Insulation</div>
    <p class="product-text">Lorem ipsum dolor sit amet, consectetur adipisicing elit, sed do eiusmod tempor.</p>
  </div>
  <div class="product" style="left:15px;top:124px">
    <div class="product-thumb" role="img" aria-label="Solar panel against blue sky" style="background:linear-gradient(135deg,#9cc4ea,#2a5d9a)"></div>
    <div class="product-name">Solar Panels</div>
    <p class="product-text">Lorem ipsum dolor sit amet, consectetur adipisicing elit, sed do eiusmod tempor.</p>
  </div>
  <div class="product" style="left:237px;top:124px">
    <div class="product-thumb" role="img" aria-label="Underfloor heating pipes" style="background:linear-gradient(135deg,#a9a49c,#5d5a55)"></div>
    <div class="product-name">Underfloor Heating</div>
    <p class="product-text">Lorem ipsum dolor sit amet, consectetur adipisicing elit, sed do eiusmod tempor.</p>
  </div>

  <div class="testimonial" style="top:58px">
    <span class="quote-open">“</span>
    <p>Sed ut perspiciatis unde omnis iste natus error sit voluptatem accusantium doloremque laudantium, totam rem aperiam, eaque.- <b>Corwin Halberd</b></p>
    <span class="quote-close">”</span>
  </div>
  <div class="testimonial" style="top:126px">
    <span class="quote-open">“</span>
    <p>Sed ut perspiciatis unde omnis iste natus error sit voluptatem accusantium doloremque laudantium, totam rem aperiam, eaque.- <b>Tamsin Orrell</b></p>
    <span class="quote-close">”</span>
  </div>
</section>

<footer class="site-footer">
  <nav class="footer-nav">
    <a href="#">Home</a><span>|</span><a href="#">What’s Blue Pact</a><span>|</span><a href="#">Homeowners</a><span>|</span><a href="#">Tenanats</a><span>|</span><a href="#">Landlords</a><span>|</span><a href="#">Book Assessment</a><span>|</span><a href="#">Contact Us</a>
  </nav>
  <p class="copyright">Copyright © 2013 Leafridge Energy</p>
</footer>
</body>
</html>
```